Logo alteration and design business card.

I want to make minor alterations to a logo that has already been designed and use the modified logo as part of the design of the business card.

Alterations to be made are as follows:
16-6240 TPX For the top green and bottom green dot.
16-4535 TPX For the Bottom blue and top blue dot
13-0220 TPX For the green outline.
13-5313 TPX For the middle line and the writing.

Particulars such as name, phone number and email to be generic for now so we can update and individualize them later. Website is www.orbivale.com.au

Target Market(s)

Men and Women 25-35 interested in ecofriendly/green products that have a positive vibe and message.

Industry/Entity Type

Business

Font styles to use
Script

Colors
0492cd
85cae6
00a98f
86cfc6

Requirements
Must have
• The modified Lumora Vista logo.
Nice to have
• We're looking for a design that is either nature based eg. bamboo, birds, trees, water, natural scenery etc. or something eg. spacey, stars, galaxy, universe etc. a positive/happy feeling to it that is quite simple and not over loaded with imagery.

```html
<!DOCTYPE html>
<html lang="en">
<head>
<meta charset="utf-8">
<title>Lumora Vista – Business Card</title>
<link href="https://fonts.googleapis.com/css2?family=Arimo:wght@400;700&display=swap" rel="stylesheet">
<style>
  :root {
    --stage: #e9eaec;
    --navy: #1b3a8c;
    --navy-deep: #142d73;
    --blue: #2b63bf;
    --brand-blue: #0492cd;
    --sky: #85cae6;
    --teal: #00a98f;
    --mint: #86cfc6;
    --leaf: #6cb33f;
    --lime: #9ccb3b;
    --paper: #ffffff;
    --ink-light: #f2f6fc;
  }
  * { box-sizing: border-box; margin: 0; padding: 0; }
  html, body {
    width: 1200px;
    height: 871px;
    overflow: hidden;
    background: var(--stage);
    font-family: "Arimo", Arial, sans-serif;
  }
  .canvas {
    position: relative;
    width: 1200px;
    height: 871px;
  }
  .card {
    position: absolute;
    width: 520px;
    height: 297px;
    border-radius: 3px;
    overflow: hidden;
    box-shadow: 0 10px 24px rgba(20, 30, 60, 0.25);
  }

  /* Front */
  .card-front {
    left: 110px;
    top: 90px;
    background: radial-gradient(circle at 50% 45%, var(--blue) 0%, var(--navy) 60%, var(--navy-deep) 100%);
  }
  .card-front .rings {
    position: absolute;
    inset: 0;
  }
  .brand {
    position: absolute;
    display: flex;
    align-items: center;
    gap: 10px;
    font-weight: 400;
    white-space: nowrap;
  }
  .brand-dot {
    display: block;
    border-radius: 50%;
    background: var(--lime);
  }
  .card-front .brand {
    left: 50%;
    top: 50%;
    transform: translate(-50%, -50%);
    color: var(--paper);
    font-size: 30px;
  }
  .card-front .brand-dot { width: 22px; height: 22px; }

  /* Back */
  .card-back {
    left: 570px;
    top: 470px;
    background: var(--navy);
  }
  .card-back .swoosh {
    position: absolute;
    inset: 0;
  }
  .card-back .brand {
    left: 34px;
    top: 118px;
    color: var(--brand-blue);
    font-size: 28px;
  }
  .card-back .brand-dot { width: 20px; height: 20px; }

  .contact {
    position: absolute;
    right: 22px;
    top: 44px;
    text-align: right;
    color: var(--ink-light);
  }
  .contact-name {
    font-size: 17px;
    font-weight: 400;
    letter-spacing: 0.3px;
  }
  .contact-role {
    font-size: 11px;
    margin-top: 2px;
  }
  .contact-address {
    font-style: normal;
    font-size: 11px;
    line-height: 1.3;
    margin-top: 24px;
  }
  .contact-lines {
    list-style: none;
    margin-top: 14px;
    font-size: 11px;
    line-height: 1.45;
  }
  .contact-lines li {
    display: flex;
    justify-content: flex-end;
    align-items: center;
    gap: 8px;
  }
  .contact-lines svg {
    width: 10px;
    height: 10px;
    fill: none;
    stroke: var(--ink-light);
    stroke-width: 1.4;
  }
</style>
</head>
<body>
<main class="canvas">

  <section class="card card-front" aria-label="Card front">
    <svg class="rings" viewBox="0 0 520 297" aria-hidden="true">
      <g fill="none" stroke="#ffffff" stroke-opacity="0.07" stroke-width="6">
        <circle cx="260" cy="135" r="90"/>
        <circle cx="260" cy="135" r="130"/>
        <circle cx="260" cy="135" r="175"/>
      </g>
    </svg>
    <div class="brand">
      <span class="brand-dot"></span>
      <span class="brand-name">Lumora Vista</span>
    </div>
  </section>

  <section class="card card-back" aria-label="Card back">
    <svg class="swoosh" viewBox="0 0 520 297" preserveAspectRatio="none" aria-hidden="true">
      <defs>
        <linearGradient id="backBlue" x1="0" y1="0" x2="1" y2="1">
          <stop offset="0" stop-color="#2e6ec8"/>
          <stop offset="1" stop-color="#1a3a8a"/>
        </linearGradient>
      </defs>
      <rect width="520" height="297" fill="url(#backBlue)"/>
      <path d="M0 0 H300 C410 80 370 235 225 297 H0 Z" fill="var(--leaf)"/>
      <path d="M0 0 H288 C396 82 356 232 212 297 H0 Z" fill="var(--sky)"/>
      <path d="M0 0 H276 C382 84 338 236 176 297 H0 Z" fill="var(--brand-blue)"/>
      <path d="M0 0 H272 C376 86 326 230 150 290 H0 Z" fill="var(--paper)"/>
    </svg>

    <div class="brand">
      <span class="brand-dot"></span>
      <span class="brand-name">Lumora Vista</span>
    </div>

    <div class="contact">
      <p class="contact-name">Rian Calder</p>
      <p class="contact-role">Director</p>
      <address class="contact-address">
        Fernleigh House<br>
        14 Marlow Lane<br>
        Bristol BS4 2TN
      </address>
      <ul class="contact-lines">
        <li>xxx - xxx - xxx
          <svg viewBox="0 0 10 10"><rect x="2.5" y="0.8" width="5" height="8.4" rx="1"/></svg>
        </li>
        <li>xxx - xxx - xxx
          <svg viewBox="0 0 10 10"><path d="M1 3 Q5 0 9 3 L8 4.5 L6.5 3.8 V3 H3.5 V3.8 L2 4.5 Z M2 9 H8 L7 5.5 H3 Z"/></svg>
        </li>
        <li>rian@orbivale.com.au
          <svg viewBox="0 0 10 10"><rect x="0.8" y="2" width="8.4" height="6"/><path d="M0.8 2 L5 5.5 L9.2 2"/></svg>
        </li>
        <li>www.orbivale.com.au
          <svg viewBox="0 0 10 10"><circle cx="5" cy="5" r="4"/><path d="M1 5 H9 M5 1 Q2.5 5 5 9 Q7.5 5 5 1"/></svg>
        </li>
      </ul>
    </div>
  </section>

</main>
</body>
</html>
```